Business Card for Financial Asset Management Company

Now we are launching a new company based in Tokyo.
The company information is below;

Company Name: Caldera Stewardship

Operations: Financial assets management, Proposing forming portfolio of assets, Consulting service, and advising to enhance your company's financial health

Corporate Colour: Japan Blue or Navy like below
http://pages.art.velmoreu.edu/tkovan/images/Indigo/Aqua-Indigo-104.jpg

It's dark and deep, and will get to fit to our clients as our relationships last longer and longer.

Our images for this colour are "Japanese style" and "pride in our craftmanship" , and also "gentle".

Corporate Key Image: an order taker who is sincere, polite, but courageous

We don't have our logo yet so please feel free to put any symbol on your design.

Please do not hesitate about asking any questions.
Thank you :-)

Reason: We are still discussin on final decision. Thank you for your understanding.

```html
<!DOCTYPE html>
<html lang="en">
<head>
<meta charset="UTF-8">
<title>Caldera Stewardship – Business Card</title>
<link href="https://fonts.googleapis.com/css2?family=Open+Sans:wght@300;400;600&display=swap" rel="stylesheet">
<style>
  :root {
    --blue-core: #0a7ccb;
    --blue-mid: #0763b8;
    --blue-edge: #0a48a3;
    --wave-top: rgba(40, 130, 215, 0.55);
    --wave-mid: rgba(30, 105, 200, 0.6);
    --wave-deep: rgba(14, 76, 170, 0.85);
    --white: #ffffff;
  }
  * { margin: 0; padding: 0; box-sizing: border-box; }
  html, body {
    width: 1200px;
    height: 726px;
    overflow: hidden;
    background: var(--blue-edge);
  }
  .card {
    position: relative;
    width: 1200px;
    height: 726px;
    overflow: hidden;
    background: radial-gradient(ellipse 640px 520px at 600px 330px, var(--blue-core) 0%, var(--blue-mid) 55%, var(--blue-edge) 100%);
    font-family: "Open Sans", Arial, sans-serif;
    color: var(--white);
  }
  .wave-band {
    position: absolute;
    left: 0;
    top: 438px;
    width: 1200px;
    height: 288px;
    background:
      linear-gradient(180deg, var(--wave-top) 0%, var(--wave-mid) 40%, var(--wave-deep) 100%);
    border-top: 2px solid rgba(70, 150, 225, 0.35);
  }
  .brand-mark {
    position: absolute;
    left: 528px;
    top: 128px;
    width: 144px;
    height: 144px;
    border-radius: 50%;
    background: var(--white);
  }
  .brand-name {
    position: absolute;
    left: 0;
    top: 262px;
    width: 1200px;
    text-align: center;
  }
  .brand-name .line-1 {
    display: block;
    font-size: 66px;
    font-weight: 600;
    line-height: 70px;
  }
  .brand-name .line-2 {
    display: block;
    font-size: 50px;
    font-weight: 300;
    line-height: 56px;
    margin-top: -6px;
  }
  .tagline {
    position: absolute;
    left: 0;
    top: 531px;
    width: 1200px;
    text-align: center;
    font-size: 29px;
    font-weight: 600;
    letter-spacing: 0.3px;
  }
  .divider {
    position: absolute;
    left: 407px;
    top: 593px;
    width: 383px;
    height: 2px;
    background: var(--white);
  }
  .website {
    position: absolute;
    left: 0;
    top: 617px;
    width: 1200px;
    text-align: center;
    font-size: 23px;
    font-weight: 400;
    letter-spacing: 0.4px;
  }
</style>
</head>
<body>
  <div class="card">
    <div class="wave-band" role="img" aria-label="Japanese seigaiha wave pattern of layered blue arcs across the lower band"></div>
    <div class="brand-mark"></div>
    <div class="brand-name">
      <span class="line-1">Caldera</span>
      <span class="line-2">Stewardship</span>
    </div>
    <p class="tagline">Financial Assets . Proposing Portfolio . Consulting Services</p>
    <div class="divider"></div>
    <p class="website">www.calderastewardship.jp</p>
  </div>
</body>
</html>
```